New Startup IT services website

We are looking for a designer to design and create a ‘child worpress’ design based on the pixelmarket-4820317-lumina-responsive-wordpress-theme (http://pixelmarket-example.net/item/lumina-responsive-wordpress-theme/4820317) . We have previously purchased this. We are looking for a front page and sub page design and coding.

That said, if you have a theme you believe would better suit our needs we are open to suggestions.

brightlinqIT is a start-up IT company whose vision is ‘To be the trusted technology service provider of choice for every business in the health industry in SEQ.’

We are focusing on the health sector by which we mean – doctors, dentists, physiotherapists, chiropractors, natural and alternative medicine, radiology, pathology, specialists etc

Please see the attached images for our logo and business card design for colour ideas etc. This website should have a professional focus. Please see the slider below.

Target Market(s)

doctors, dentists, physiotherapists, chiropractors, natural and alternative medicine, radiology, pathology, specialists etc

Requirements
Must have
• The front page elements should include the following :-
• Menu Structure will consist of
• HOME / OUR APPROACH / SERVICES / PARTNERS / FAQ / CONTACT US
• ------------------
• Menu Slider (picture window)
• Design (with images) the following 4 graphics and text
• 1. After Hours approach – We do our work, when you’re not doing yours.
• 2. FREE 32 point checklist – How reliable is your technology really?
• 3. We Specialize in Security and protecting your patients confidentiality
• 4. The Cloud – Buzzword or the future? Ask us what you can and can’t do with it.
• -------------------
• 3 FEATURES
• Here we want a section where we show three major features of our company. These are just a snapshot which will link to background pages. The three areas are:
• 1. Complete Services – What we offer
• 2. New Practise – We specialise in setting up new medical practises.
• 3. Our Approach / unique / we do our work, when you’re not doing yours.
• -------------------
• We would like a small text area (no more than 100 words) for us to introduce brightlinkIT as a services company.
• -------------------
• Partners Logos – A small area on the front screen page where we can promote the major partners we work with. Will Also link to Partners Page
• -------------------
• Footer
• To include site map, privacy policy, ABN (which is an Australian business number) copyright message

```html
<!DOCTYPE html>
<html lang="en">
<head>
<meta charset="utf-8">
<title>brightlinkIT – IT services for the health sector</title>
<link rel="stylesheet" href="https://fonts.googleapis.com/css2?family=Source+Sans+3:ital,wght@0,400;0,600;0,700;1,400&family=Crimson+Text:ital@1&display=swap">
<style>
:root{
  --blue:#2b4f8e;
  --blue-link:#1f7fc4;
  --blue-icon:#2a86c8;
  --orange:#d9803a;
  --text:#555;
  --muted:#777;
  --line:#e2e2e2;
  --band:#f4f4f4;
  --footer:#ebebeb;
  --bar:#363636;
}
*{box-sizing:border-box;margin:0;padding:0}
html,body{width:802px;height:1200px;overflow:hidden;background:#fff}
body{position:relative;font-family:"Source Sans 3",Arial,sans-serif;color:var(--text)}
.abs{position:absolute}

/* header */
.brand{left:101px;top:22px;font-size:28px;line-height:32px;font-weight:600;color:var(--blue-icon);letter-spacing:-0.3px}
.call{right:67px;top:20px;font-size:15px;color:#999}
.call strong{color:var(--blue);font-weight:400}
.nav{right:67px;top:47px;display:flex;gap:14px;font-size:10px;color:#333;text-transform:uppercase}
.nav a{color:inherit;text-decoration:none;line-height:16px;padding:0 5px}
.nav a.active{background:#1d68b0;color:#fff;border-radius:2px}

/* hero */
.hero{left:0;top:92px;width:802px;height:254px;background:radial-gradient(ellipse at 60% 40%,#fff 0%,#f2f2f2 55%,#e2e2e2 100%);border-bottom:1px solid #ddd}
.hero h1{position:absolute;left:81px;top:64px;font-size:31px;font-weight:700;color:var(--blue);letter-spacing:-0.5px}
.hero p{position:absolute;left:81px;top:104px;font-size:15px;color:#555}
.btn-contact{position:absolute;left:81px;top:134px;width:105px;height:30px;background:linear-gradient(#e9a45f,#d3813a);border-radius:2px;color:#fff;font-size:13px;line-height:30px;text-align:center}
.hero-art{position:absolute;left:444px;top:52px;width:232px;height:160px;border-radius:10px;background:linear-gradient(135deg,#e6e8ea,#cfd4d8 60%,#3a9fd6)}
.dots{position:absolute;left:78px;top:224px;display:flex;gap:6px}
.dots span{width:10px;height:10px;border-radius:50%;background:#999}
.dots span:first-child{background:#666}

/* focus band */
.focus{left:0;top:346px;width:802px;height:58px;background:var(--band)}
.focus h2{position:absolute;left:190px;top:15px;font-size:20px;font-weight:400;color:var(--orange)}
.know{position:absolute;left:514px;top:20px;width:80px;height:20px;border:1px solid #ccc;background:#fff;border-radius:2px;font-size:9px;color:#444;line-height:18px;padding-left:9px}
.know svg{position:absolute;right:6px;top:4px}

/* intro */
.thumb{top:437px;width:145px;height:87px;border:1px solid #ddd}
.thumb.lab{left:77px;background:linear-gradient(135deg,#6aa6d6,#cfe3f2 50%,#3e6e9e)}
.thumb.steth{left:246px;background:linear-gradient(135deg,#f4f6f8,#dfe8f0 55%,#2c6db4)}
.caption{top:533px;width:150px;font-size:10px;line-height:15px;color:var(--blue-link)}
.welcome{left:414px;top:432px;font-size:19px;color:var(--blue);font-weight:400}
.welcome b{font-weight:700}
.intro{left:414px;top:465px;width:314px;font-size:9.6px;line-height:16.8px;text-align:justify}

.rule{left:69px;width:665px;height:1px;background:var(--line)}
.quote{left:88px;top:614px;width:625px;font-family:"Crimson Text",Georgia,serif;font-style:italic;font-size:15.5px;line-height:21px;color:#8d9bbf;padding-left:27px}
.quote .open{position:absolute;left:0;top:0;font-size:26px;line-height:26px;font-style:normal;font-weight:700}
.quote .close{display:inline-block;margin-left:4px;font-size:26px;line-height:14px;vertical-align:-8px;font-style:normal;font-weight:700}

/* services */
.svc{width:200px}
.svc svg{position:absolute;left:0;top:2px}
.svc h3{margin-left:36px;font-size:15px;font-weight:400;color:var(--blue);line-height:17px;min-height:34px;display:flex;align-items:center}
.svc p{margin-top:10px;font-size:8.8px;line-height:14px;color:#555}
.vline{width:1px;background:var(--line)}

/* partners */
.partners{left:69px;top:978px;width:665px;display:flex;justify-content:space-between;align-items:center}
.partners span{font-size:18px;font-weight:700;color:#24479a;letter-spacing:0.5px}
.partners span:last-child{color:#111}

/* footer */
.footer{left:0;top:1038px;width:802px;height:130px;background:var(--footer)}
.fcol{top:14px;font-size:8.8px;color:#444;line-height:17.5px}
.fcol h4{font-size:10px;font-weight:400;color:var(--orange);margin-bottom:2px}
.blog-title{font-size:10px;color:#222}
.blog p{color:#666;width:150px;text-align:justify;line-height:14px}
.social div{display:flex;align-items:center;gap:6px;color:#888;font-size:9.4px;line-height:20px}
.social i{width:15px;height:15px;border-radius:2px;display:inline-block}
.bar{left:0;top:1168px;width:802px;height:32px;background:var(--bar);color:#ddd;font-size:9px;line-height:32px}
.bar .links{position:absolute;left:67px}
.bar .copy{position:absolute;right:67px}
</style>
</head>
<body>

<header>
  <div class="abs brand">brightlinkIT</div>
  <div class="abs call">Call us : <strong>(07) 5550 1847</strong></div>
  <nav class="abs nav">
    <a class="active">Home</a><a>Our Approach</a><a>Services</a><a>Partners</a><a>FAQ</a><a>Contact Us</a>
  </nav>
</header>

<section class="abs hero">
  <h1>After Hours approach</h1>
  <p>We do our work, when your not doing yours</p>
  <div class="btn-contact">Contact us Now</div>
  <div class="hero-art" role="img" aria-label="Illustration of blue figures assembling white puzzle pieces"></div>
  <div class="dots"><span></span><span></span><span></span><span></span></div>
</section>

<section class="abs focus">
  <h2>We are focusing on the health sector</h2>
  <div class="know">KNOW MORE
    <svg width="11" height="11" viewBox="0 0 12 12"><circle cx="6" cy="6" r="5" fill="none" stroke="#555" stroke-width="1.2"/><path d="M3.5 6h5M6.5 4l2 2-2 2" fill="none" stroke="#555" stroke-width="1.2"/></svg>
  </div>
</section>

<div class="abs thumb lab" role="img" aria-label="Photo of a scientist with a microscope and molecule model"></div>
<div class="abs caption" style="left:77px">Phasellus sagittis luctus vestibulum turpis et turpis gravida.</div>
<div class="abs thumb steth" role="img" aria-label="Photo of a stethoscope on financial charts"></div>
<div class="abs caption" style="left:246px">Phasellus sagittis luctus vestibulum turpis et turpis gravida.</div>
<h2 class="abs welcome">Welcome to <b>BrightlinqIT</b></h2>
<p class="abs intro">Donec eleifend condimentum molestie. Quisque rhoncus bibendum lorem ac pretium. Integer accumsan metus ante, ac lacinia dolor tincidunt et. Proin pel lentesque est lorem, nec tristique nulla bibendum id. Maecenas vitae bibendum enim. Nulla facilisi. Aliquam volutpat arcu vel orci pharetra, sit amet cursus leo vestibulum. Lorem ipsum dolor sit amet, consectetur adipiscing elit. Phasellus sagittis luctus vestibulum turpis et turpis gravida.</p>

<div class="abs rule" style="top:596px"></div>
<blockquote class="abs quote"><span class="open">&ldquo;</span>Mauris vel lacus vitae felis vestibulum volutpat Etiam est nunc venenatis in tristique eu imperdiet ac nisl Cum sociis natoque penatibus et magnis dis parturient montes,<span class="close">&rdquo;</span></blockquote>
<div class="abs rule" style="top:680px"></div>

<section>
  <div class="abs svc" style="left:94px;top:713px">
    <svg width="24" height="24" viewBox="0 0 24 24"><rect x="2" y="3" width="20" height="14" rx="1" fill="var(--blue-icon)"/><rect x="4" y="5" width="16" height="10" fill="#fff"/><rect x="9" y="18" width="6" height="3" fill="var(--blue-icon)"/></svg>
    <h3>Heathcare Softwares Development</h3>
    <p>Fusce quis ligula ut risus eleifend posuere. Integer fermentum ligula accumsan egestas turpis sapien, vitae feugiat dolor.</p>
  </div>
  <div class="abs svc" style="left:318px;top:713px">
    <svg width="24" height="24" viewBox="0 0 24 24"><circle cx="12" cy="12" r="10" fill="var(--blue-icon)"/><path d="M6 8c3 0 4 2 3 4s2 3 1 6M14 5c1 2 4 2 5 4" fill="none" stroke="#fff" stroke-width="1.6"/></svg>
    <h3>Web Access Services</h3>
    <p>Fusce quis ligula ut risus eleifend posuere. Integer fermentum ligula accumsan egestas turpis sapien, vitae feugiat dolor.</p>
  </div>
  <div class="abs svc" style="left:542px;top:713px">
    <svg width="24" height="24" viewBox="0 0 24 24"><rect x="7" y="3" width="10" height="6" fill="var(--blue-icon)"/><rect x="3" y="9" width="18" height="8" rx="1" fill="var(--blue-icon)"/><rect x="7" y="14" width="10" height="6" fill="#fff" stroke="var(--blue-icon)" stroke-width="1.5"/></svg>
    <h3>Hospital Equipments</h3>
    <p>Fusce quis ligula ut risus eleifend posuere. Integer fermentum ligula accumsan egestas turpis sapien, vitae feugiat dolor.</p>
  </div>

  <div class="abs vline" style="left:290px;top:712px;height:92px"></div>
  <div class="abs vline" style="left:514px;top:712px;height:92px"></div>
  <div class="abs rule" style="left:87px;width:180px;top:818px"></div>
  <div class="abs rule" style="left:311px;width:180px;top:818px"></div>
  <div class="abs rule" style="left:540px;width:180px;top:818px"></div>
  <div class="abs vline" style="left:290px;top:832px;height:90px"></div>
  <div class="abs vline" style="left:514px;top:832px;height:90px"></div>

  <div class="abs svc" style="left:94px;top:833px">
    <svg width="24" height="24" viewBox="0 0 24 24"><circle cx="12" cy="6" r="4" fill="var(--blue-icon)"/><path d="M5 22v-6c0-3 3-5 7-5s7 2 7 5v6z" fill="var(--blue-icon)"/></svg>
    <h3>Hospital Workers &amp; Doctors Recruitments</h3>
    <p>Fusce quis ligula ut risus eleifend posuere. Integer fermentum ligula accumsan egestas turpis sapien, vitae feugiat dolor.</p>
  </div>
  <div class="abs svc" style="left:318px;top:833px">
    <svg width="24" height="24" viewBox="0 0 24 24"><rect x="4" y="2" width="16" height="20" rx="2" fill="var(--blue-icon)"/><circle cx="12" cy="12" r="5" fill="#fff"/><circle cx="12" cy="12" r="2" fill="var(--blue-icon)"/></svg>
    <h3>Hospital Data Security</h3>
    <p>Fusce quis ligula ut risus eleifend posuere. Integer fermentum ligula accumsan egestas turpis sapien, vitae feugiat dolor.</p>
  </div>
  <div class="abs svc" style="left:542px;top:833px">
    <svg width="24" height="24" viewBox="0 0 24 24"><circle cx="12" cy="12" r="10" fill="var(--blue-icon)"/><circle cx="12" cy="12" r="4.5" fill="#fff"/><path d="M12 2v5M12 17v5M2 12h5M17 12h5" stroke="#fff" stroke-width="2.4"/></svg>
    <h3>Technology Support</h3>
    <p>Fusce quis ligula ut risus eleifend posuere. Integer fermentum ligula accumsan egestas turpis sapien, vitae feugiat dolor.</p>
  </div>
</section>

<div class="abs rule" style="top:960px"></div>
<section class="abs partners" aria-label="Partners">
  <span>Vantrix</span><span>Orbel</span><span>Kestrelnet</span><span>Dunmore</span><span>Halvio</span><span>Soreno</span>
</section>

<footer class="abs footer">
  <div class="abs fcol" style="left:78px">
    <h4>Contact us</h4>
    <div>55 Building name, Street name</div>
    <div>City - zip code</div>
    <div>Call us : 555 321 0199</div>
    <div>Fax &nbsp;&nbsp;: 555 213 0274</div>
    <div>E-mail : info@brightlinkit-example.com</div>
  </div>
  <div class="abs fcol" style="left:239px">
    <h4>Quick Links</h4>
    <div>» Donec dictum</div>
    <div>» Mauris varius lorem</div>
    <div>» Donec sed fermentum ligula</div>
    <div>» Quisque rhoncus</div>
    <div>» Nam mollis risus eleifend</div>
  </div>
  <div class="abs fcol blog" style="left:400px">
    <h4>Latest Blog</h4>
    <div class="blog-title">Quisque rhoncus bibendum lorem</div>
    <p>Fusce quis eleifend posuere. Integer fermentum ligula accumsan ate egestas turpis sapien, vitae feugiat dolor.</p>
    <div>October - 6 - 2013</div>
  </div>
  <div class="abs fcol social" style="left:596px">
    <h4>Connect with us</h4>
    <div><i style="background:#4a66a0"></i>Join with us on &nbsp;Socialbook</div>
    <div><i style="background:#3fb3e6"></i>Follow us on &nbsp;Chirper</div>
    <div><i style="background:#1a73a8"></i>Share on &nbsp;Linkwork</div>
    <div><i style="background:#d8d8d8"></i>Contact us by E-mail</div>
  </div>
</footer>

<div class="abs bar">
  <div class="links">HOME / OUR APPROACH / SERVICES / PARTNERS / FAQ / CONTACT US</div>
  <div class="copy">Copyright © 2013 &nbsp;brightlinkIT. &nbsp;All rights reserved. &nbsp;&nbsp;Sitemap &nbsp;| &nbsp;Privacy Policy</div>
</div>

</body>
</html>
```